Forestry Mulching Business Cards

Business is called Timberline Clearing, We do forestry mulching which helps with wildfire mitigation, it helps reclaim your land. Just some ideas on what to say, get creative. I would like a Ravlex tracked skidsteer with a mulching head on it included somewhere, like the one i have attached in the photo. I would also like to add a groundhog popping out of the ground as a logo since i do not have one yet. Name and phone number and location should have a text slot, maybe include what brush removal/control does for you on the back in bulletins. I know i didnt make this very detailed but i want you guys to get creative!

```html
<!DOCTYPE html>
<html lang="en">
<head>
<meta charset="UTF-8">
<title>Timberline Clearing – Business Cards</title>
<link rel="stylesheet" href="https://fonts.googleapis.com/css2?family=Barlow+Condensed:wght@400;500&family=Rubik:wght@300;800&display=swap">
<style>
  :root {
    --orange: #e84e1c;
    --ink: #1d1d1b;
    --paper: #ffffff;
    --backdrop: #e4e5e1;
    --photo-dark: #3a3a3c;
    --photo-light: #d9d9d6;
  }
  * { margin: 0; padding: 0; box-sizing: border-box; }
  html, body {
    width: 1200px; height: 1200px; overflow: hidden;
    background: var(--backdrop);
  }
  .sheet { position: relative; width: 1200px; height: 1200px; }

  .card {
    position: absolute; left: 175px; width: 873px; height: 499px;
    overflow: hidden;
  }
  .card--front { top: 43px; background: var(--paper); }
  .card--back { top: 615px; background: var(--orange); }

  .card__band {
    position: absolute; left: 0; bottom: 0; width: 100%; height: 17px;
  }
  .card--front .card__band { background: var(--orange); }
  .card--back .card__band { background: var(--ink); }

  /* Front: brand */
  .brand {
    position: absolute; left: 52px; top: 87px; width: 326px; height: 193px;
    display: flex; flex-direction: column; align-items: center; justify-content: center;
    gap: 14px;
  }
  .brand__dot {
    width: 96px; height: 96px; border-radius: 50%; background: var(--orange);
  }
  .brand__name {
    font-family: "Rubik", sans-serif; font-weight: 800; color: var(--orange);
    font-size: 38px; line-height: 1.02; text-align: center; text-transform: uppercase;
  }

  .divider {
    position: absolute; left: 436px; top: 73px; width: 1px; height: 242px;
    background: var(--ink);
  }

  .contact { position: absolute; left: 0; top: 0; list-style: none; }
  .contact__row {
    position: absolute; left: 500px; display: flex; align-items: center;
    font-family: "Barlow Condensed", sans-serif; color: var(--ink);
    white-space: nowrap; transform: translateY(-50%);
  }
  .contact__icon { width: 18px; height: 18px; margin-right: 6px; flex: none; fill: var(--orange); }
  .contact__row--name { top: 129px; font-size: 31px; font-weight: 500; }
  .contact__row--address { top: 182px; font-size: 22px; }
  .contact__row--phone { top: 222px; font-size: 22px; }
  .contact__row--email { top: 261px; font-size: 22px; }

  .tagline {
    position: absolute; left: 0; width: 100%; top: 427px; transform: translateY(-50%);
    text-align: center; font-family: "Rubik", sans-serif; font-weight: 300;
    font-size: 36px; color: var(--ink); white-space: nowrap;
  }

  /* Back */
  .benefits__title {
    position: absolute; left: 55px; top: 36px;
    font-family: "Rubik", sans-serif; font-weight: 800; color: var(--paper);
    font-size: 40px; line-height: 50px; text-transform: uppercase; white-space: nowrap;
  }
  .benefits__list { position: absolute; left: 55px; top: 0; list-style: none; }
  .benefits__item {
    position: absolute; left: 0; display: flex; align-items: center; white-space: nowrap;
    transform: translateY(-50%);
    font-family: "Barlow Condensed", sans-serif; font-size: 30px; color: var(--paper);
  }
  .benefits__tick { width: 24px; height: 20px; margin-right: 23px; fill: none; stroke: var(--ink); stroke-width: 5; }

  .machine-photo {
    position: absolute; left: 424px; top: 167px; width: 401px; height: 292px;
    border-radius: 6px;
    background: linear-gradient(160deg, var(--photo-light) 0%, #9c9c9c 45%, var(--photo-dark) 100%);
  }
</style>
</head>
<body>
<div class="sheet">

  <section class="card card--front">
    <div class="brand">
      <span class="brand__dot"></span>
      <span class="brand__name">Timberline<br>Clearing</span>
    </div>

    <div class="divider"></div>

    <ul class="contact">
      <li class="contact__row contact__row--name" style="top:129px">
        <svg class="contact__icon" viewBox="0 0 20 20"><circle cx="10" cy="6" r="4"/><path d="M2 19c0-5 3.5-7 8-7s8 2 8 7z"/></svg>
        Name
      </li>
      <li class="contact__row contact__row--address">
        <svg class="contact__icon" viewBox="0 0 20 20"><path d="M10 1a7 7 0 0 0-7 7c0 5 7 11 7 11s7-6 7-11a7 7 0 0 0-7-7zm0 10a3 3 0 1 1 0-6 3 3 0 0 1 0 6z"/></svg>
        Address line here
      </li>
      <li class="contact__row contact__row--phone">
        <svg class="contact__icon" viewBox="0 0 20 20"><path d="M5 1l3 4-2 3c1 2 3 4 5 5l3-2 4 3-2 4C9 18 2 11 1 3z"/></svg>
        000 111 2222
      </li>
      <li class="contact__row contact__row--email">
        <svg class="contact__icon" viewBox="0 0 20 20"><rect x="1" y="4" width="18" height="13" rx="1"/><path d="M3 6l7 5 7-5" fill="none" stroke="#fff" stroke-width="1.6"/></svg>
        name@emailaddress.com
      </li>
    </ul>

    <p class="tagline">FORESTRY MULCHING AND BRUSH CONTROL</p>
    <div class="card__band"></div>
  </section>

  <section class="card card--back">
    <h2 class="benefits__title">What brush removal / control<br>can do for you</h2>

    <ul class="benefits__list">
      <li class="benefits__item" style="top:183px"><svg class="benefits__tick" viewBox="0 0 24 20"><path d="M2 10l7 7L22 3"/></svg>Wildfire mitigation</li>
      <li class="benefits__item" style="top:224px"><svg class="benefits__tick" viewBox="0 0 24 20"><path d="M2 10l7 7L22 3"/></svg>Environmentally friendly</li>
      <li class="benefits__item" style="top:265px"><svg class="benefits__tick" viewBox="0 0 24 20"><path d="M2 10l7 7L22 3"/></svg>Prevents soil erosion</li>
      <li class="benefits__item" style="top:306px"><svg class="benefits__tick" viewBox="0 0 24 20"><path d="M2 10l7 7L22 3"/></svg>Improves soil quality</li>
      <li class="benefits__item" style="top:348px"><svg class="benefits__tick" viewBox="0 0 24 20"><path d="M2 10l7 7L22 3"/></svg>Weed and pest control</li>
      <li class="benefits__item" style="top:389px"><svg class="benefits__tick" viewBox="0 0 24 20"><path d="M2 10l7 7L22 3"/></svg>Fast and efficient</li>
      <li class="benefits__item" style="top:431px"><svg class="benefits__tick" viewBox="0 0 24 20"><path d="M2 10l7 7L22 3"/></svg>Cost effective</li>
    </ul>

    <div class="machine-photo" role="img" aria-label="Photo of a white Ravlex tracked skid steer fitted with a black forestry mulching head"></div>

    <div class="card__band"></div>
  </section>

</div>
</body>
</html>
```